Psychology and personal development service needs an awesome Web Design

Hi, we are Bright Path Studio, a psychology and personal development service located in Melbourne Australia. We already have a website www.brightpathstudio.org but it is in great need of a makeover! We add to the website regularly with articles and so we need a space to archive these when they come off the main page, and we have products that we would like to sell internationally so we need a shop page that can convert currencies for international sales and calculate postage and handling. We have a Chatterly page that we would like to link as well as a newsletter that we would like to archive on the website. We have just had a logo designed through mark forge and would like to incorporate this into our website. We want something with high visual impact and uncluttered.
We also run workshops and events so need a tab for this.
Thanks for getting on board!

```html
<!DOCTYPE html>
<html lang="en">
<head>
<meta charset="utf-8">
<title>Bright Path Studio</title>
<link href="https://fonts.googleapis.com/css2?family=Lato:wght@400;700&family=Lora:ital,wght@0,400;0,700;1,400&display=swap" rel="stylesheet">
<style>
:root{
  --teal:#3fb8b0;
  --teal-soft:#8fd3cf;
  --pink:#e0458f;
  --purple:#6c5aa8;
  --purple-deep:#5b4a99;
  --blue:#3b96c9;
  --ink:#3d3d3d;
  --grey-bg:#eff2f2;
  --line:#e3e3e3;
  --white:#fff;
}
*{box-sizing:border-box;margin:0;padding:0}
html,body{width:1119px;height:1200px;overflow:hidden}
body{position:relative;background:var(--white);font-family:"Lato",sans-serif;color:var(--ink)}
.abs{position:absolute}
a{color:inherit;text-decoration:none}

/* header */
.header{left:0;top:0;width:1119px;height:96px;background:var(--white)}
.header-rule{left:0;top:96px;width:1119px;height:3px;background:linear-gradient(90deg,var(--teal),var(--purple),var(--pink))}
.brand{left:229px;top:24px;display:flex;align-items:center;gap:10px}
.brand-dot{width:44px;height:44px;border-radius:50%;background:var(--purple);flex:none}
.brand-name{font-family:"Lora",serif;font-size:20px;color:var(--purple);line-height:1.05;width:110px}
.like-box{left:617px;top:23px;width:44px;text-align:center}
.like-count{border:1px solid #c9cdd6;border-radius:3px;font-size:11px;color:#555;padding:3px 0;background:#fff}
.like-btn{margin-top:6px;background:#4d67a0;color:#fff;font-size:9px;font-weight:700;border-radius:2px;padding:3px 0}
.util{left:690px;top:53px;width:210px;height:12px;font-size:8px;letter-spacing:.6px;color:#555;text-transform:uppercase}
.util > *{position:absolute;top:0;line-height:11px}
.util .social{top:2px;width:7px;height:7px;border-radius:50%;background:#555}
.util .sep{top:1px;width:1px;height:10px;background:var(--line)}

/* nav */
.nav{left:0;top:99px;width:1119px;height:35px;background:var(--grey-bg)}
.nav ul{position:absolute;left:229px;top:12px;display:flex;gap:29px;list-style:none;font-family:"Lora",serif;font-size:9.5px;letter-spacing:.5px;color:#444;text-transform:uppercase}
.nav svg{position:absolute;left:881px;top:12px}

/* hero */
.hero{left:0;top:134px;width:1119px;height:210px;background:linear-gradient(95deg,#4aa9a8 0%,#6e8fbd 30%,#7f6fb6 55%,#c066ad 80%,#e0528f 100%)}
.hero-book{left:309px;top:21px;width:74px;height:166px;background:linear-gradient(160deg,#4b4b4b,#1f1f1f 60%,#3a3a3a);box-shadow:4px 4px 10px rgba(0,0,0,.35)}
.hero-title{left:452px;top:49px;font-family:"Lora",serif;font-style:italic;font-weight:400;font-size:22px;color:var(--white);white-space:nowrap}
.hero-title b{font-weight:400;text-transform:uppercase}
.hero-text{left:452px;top:86px;width:300px;font-size:12.5px;line-height:16px;color:rgba(255,255,255,.9)}
.hero-btn{left:452px;top:130px;width:94px;height:23px;border-radius:12px;background:var(--teal-soft);color:#fff;font-family:"Lora",serif;font-size:10px;letter-spacing:1.5px;text-align:center;line-height:23px;box-shadow:0 2px 3px rgba(0,0,0,.15)}
.hero-arrow{width:20px;height:20px;border-radius:50%;background:var(--teal-soft);top:96px;display:flex;align-items:center;justify-content:center}

/* main */
.main-bg{left:0;top:344px;width:669px;height:615px;background:var(--grey-bg)}
.card{width:199px;height:256px;background:var(--white);border:1px solid var(--line)}
.card-photo{height:102px;margin:-1px -1px 0}
.card h3{font-family:"Lora",serif;font-weight:400;font-size:11px;margin:19px 0 0 18px;white-space:nowrap}
.card .date{margin:7px 0 0 18px;font-size:9.5px;color:#555;display:flex;align-items:center;gap:7px}
.card p{margin:8px 16px 0 18px;font-size:9px;line-height:11px;color:#555}
.card .more{position:absolute;left:18px;top:211px;width:76px;height:19px;border:1px solid #bfe3e1;border-radius:10px;font-size:7.5px;letter-spacing:.8px;text-align:center;line-height:17px;color:#555}
.card .bar{position:absolute;left:-1px;right:-1px;bottom:-3px;height:3px}
.teal h3{color:var(--teal)}.teal .bar{background:var(--teal)}
.pink h3{color:var(--pink)}.pink .bar{background:var(--pink)}
.blue h3{color:var(--blue)}.blue .bar{background:var(--blue)}
.violet h3{color:var(--purple)}.violet .bar{background:var(--purple)}

/* sidebar */
.side-head{left:686px;top:360px;font-family:"Lora",serif;font-size:9.5px;color:var(--purple)}
.side-head i{color:var(--teal);margin-left:4px}
.book-box{left:686px;top:383px;width:208px;height:140px;border:2px dotted #e5e5e5}
.book-cover{position:absolute;left:14px;top:13px;width:72px;height:112px;background:linear-gradient(150deg,#cfe4f1,#9cc3df);box-shadow:2px 2px 4px rgba(0,0,0,.2)}
.book-title{position:absolute;left:109px;top:28px;font-family:"Lora",serif;font-size:11px;line-height:12px;color:var(--purple)}
.book-price{position:absolute;left:109px;top:56px;font-size:11px;color:var(--pink)}
.dots{position:absolute;left:109px;top:81px;display:flex;gap:3px}
.dots span{width:8px;height:8px;border-radius:50%;border:1px solid #bbb}
.dots .on{background:var(--teal);border-color:var(--teal)}
.book-btn{position:absolute;left:109px;top:107px;width:65px;height:17px;border:1px solid #bfe3e1;border-radius:9px;font-size:7px;letter-spacing:.6px;text-align:center;line-height:15px;color:var(--teal)}
.news{left:686px;top:535px;width:208px;height:97px;background:var(--purple)}
.news-title{position:absolute;left:15px;top:19px;font-family:"Lora",serif;font-size:9.5px;color:#fff;letter-spacing:.4px;display:flex;gap:8px;align-items:center}
.news-title i{font-style:italic;letter-spacing:0}
.news-rule{position:absolute;left:15px;right:15px;top:38px;height:1px;background:rgba(255,255,255,.3)}
.news-field{position:absolute;left:15px;top:50px;width:108px;height:24px;background:#fff;font-size:8.5px;color:#999;text-align:center;line-height:24px}
.news-btn{position:absolute;left:123px;top:50px;width:70px;height:24px;background:var(--teal-soft);font-family:"Lora",serif;font-size:8.5px;color:#fff;font-weight:700;text-align:center;line-height:24px}
.tabs{left:686px;top:646px;width:208px;height:27px;border-bottom:1px solid var(--line)}
.tab-on{position:absolute;left:0;top:0;width:124px;height:27px;background:var(--pink);color:#fff;font-family:"Lora",serif;font-size:9.5px;text-align:center;line-height:27px}
.tab-off{position:absolute;left:135px;top:0;height:27px;color:var(--pink);font-family:"Lora",serif;font-size:9.5px;line-height:27px}
.event{left:686px;width:208px;height:80px;border-bottom:1px solid var(--line)}
.event-date{position:absolute;left:0;top:0;width:55px;height:50px;background:linear-gradient(160deg,#7f6fb6,#c066ad 55%,#3fb8b0);color:#fff;font-family:"Lora",serif;text-align:center;box-shadow:1px 2px 3px rgba(0,0,0,.2)}
.event-date .m{font-size:11px;padding-top:6px}
.event-date .d{font-size:9px;margin-top:8px}
.event-text{position:absolute;left:68px;top:2px;font-size:10px;line-height:12px;color:#444;width:140px}
.event-place{position:absolute;left:68px;top:32px;font-family:"Lora",serif;font-size:10px;color:var(--pink)}

/* footer */
.footer{left:0;top:959px;width:1119px;height:241px;background:linear-gradient(180deg,#7965b4,#6e5bad)}
.foot-brand{left:242px;top:44px;display:flex;align-items:center;gap:8px}
.foot-brand .brand-dot{background:rgba(255,255,255,.85);width:34px;height:34px}
.foot-brand .brand-name{color:#fff;font-size:15px;width:82px}
.foot-nav{left:378px;top:53px;display:flex;gap:19px;list-style:none;font-family:"Lora",serif;font-size:8px;color:#fff;letter-spacing:.4px}
.follow{left:378px;top:74px;display:flex;align-items:center;gap:8px;color:#fff;font-size:11px}
.follow span{width:18px;height:18px;border-radius:50%;border:1px solid #fff}
.copyright{left:473px;top:77px;font-size:10px;color:rgba(255,255,255,.9)}
.widget{left:686px;top:17px;width:208px;height:205px;background:#fff;border:1px solid #d0d0d0}
.widget-head{height:19px;background:var(--purple-deep);color:#fff;font-size:9px;padding:5px 10px}
.widget-page{position:absolute;left:10px;top:30px;display:flex;gap:8px}
.widget-page .pic,.post .pic{width:28px;height:28px;border-radius:50%;background:var(--purple);flex:none}
.widget-page .name,.post .name{font-size:9px;font-weight:700;color:#3b5fa0}
.widget-page .like{display:inline-block;margin-top:4px;background:#4d67a0;color:#fff;font-size:8px;font-weight:700;padding:2px 6px;border-radius:2px}
.widget-page .count{font-size:8px;font-weight:700;margin-left:6px}
.post{position:absolute;left:10px;top:87px;width:184px;height:100px;border:1px solid #ddd;padding:8px}
.post .row{display:flex;gap:8px}
.post .time{font-size:7px;color:#888;margin-top:2px}
.post p{font-size:8.5px;line-height:11px;color:#333;margin-top:10px;width:160px}
.scroll{position:absolute;right:4px;top:95px;width:6px;height:30px;background:#bbb}
</style>
</head>
<body>

<header class="abs header">
  <div class="abs brand"><span class="brand-dot"></span><span class="brand-name">Bright Path Studio</span></div>
  <div class="abs like-box"><div class="like-count">289</div><div class="like-btn">Like</div></div>
  <nav class="abs util">
    <span class="social" style="left:0" aria-label="Chatterly"></span>
    <span class="sep" style="left:12px"></span>
    <a href="#" style="left:21px">Currency</a>
    <span class="sep" style="left:69px"></span>
    <a href="#" style="left:78px">My Account</a>
    <span class="sep" style="left:136px"></span>
    <a href="#" style="left:145px">My Cart (0)</a>
    <svg style="left:199px;top:1px" width="9" height="8" viewBox="0 0 9 8"><path d="M0 0h2l1 5h5l1-4H3" fill="none" stroke="#555" stroke-width="1"/><circle cx="3.5" cy="7" r="1" fill="#555"/><circle cx="7" cy="7" r="1" fill="#555"/></svg>
  </nav>
</header>
<div class="abs header-rule"></div>

<nav class="abs nav">
  <ul><li>Home</li><li>About Us</li><li>Books</li><li>Online Store</li><li>Contact Us</li></ul>
  <svg width="10" height="10" viewBox="0 0 10 10"><circle cx="4" cy="4" r="3" fill="none" stroke="#444" stroke-width="1.5"/><path d="M6.5 6.5L9.5 9.5" stroke="#444" stroke-width="1.5"/></svg>
</nav>

<section class="abs hero">
  <div class="abs hero-arrow" style="left:229px"><svg width="8" height="8" viewBox="0 0 8 8"><path d="M5 1L2 4l3 3" fill="none" stroke="#fff" stroke-width="1.5"/></svg></div>
  <div class="abs hero-book" role="img" aria-label="Book cover of Ivy: Letters From the Cloister"></div>
  <h1 class="abs hero-title"><b>Ivy:</b> Letters From the Cloister</h1>
  <p class="abs hero-text">Co-founder of Bright Path Studio, Nora Whitfield, has just released the sequel to Steady</p>
  <a class="abs hero-btn" href="#">SHOP NOW</a>
  <div class="abs hero-arrow" style="left:874px"><svg width="8" height="8" viewBox="0 0 8 8"><path d="M3 1l3 3-3 3" fill="none" stroke="#fff" stroke-width="1.5"/></svg></div>
</section>

<div class="abs main-bg"></div>

<article class="abs card teal" style="left:230px;top:363px">
  <div class="card-photo" role="img" aria-label="Seashells on a sunny beach" style="background:linear-gradient(180deg,#9fd3ea,#e8c9a6 60%,#c98e62)"></div>
  <h3>Positive Emotion</h3>
  <div class="date"><svg width="8" height="8"><rect x=".5" y="1.5" width="7" height="6" fill="none" stroke="#666"/><rect x=".5" y="1.5" width="7" height="2" fill="#666"/></svg>October 2014</div>
  <p>We are told that our thoughts have power and that what we think about we bring aboutrun with stress</p>
  <a class="more" href="#">READ MORE</a><span class="bar"></span>
</article>
<article class="abs card pink" style="left:451px;top:363px">
  <div class="card-photo" role="img" aria-label="Grass stems against a warm sunset" style="background:linear-gradient(180deg,#e6cfae,#c9a57a 60%,#8a6a45)"></div>
  <h3>Simplicity Leads to Good Health</h3>
  <div class="date"><svg width="8" height="8"><rect x=".5" y="1.5" width="7" height="6" fill="none" stroke="#666"/><rect x=".5" y="1.5" width="7" height="2" fill="#666"/></svg>October 2014</div>
  <p>We are told that our thoughts have power and that what we think about we bring aboutrun with stress</p>
  <a class="more" href="#">READ MORE</a><span class="bar"></span>
</article>
<article class="abs card blue" style="left:230px;top:642px">
  <div class="card-photo" role="img" aria-label="Dark pebbles with an orange leaf" style="background:linear-gradient(135deg,#555,#2b2b2b 50%,#4a4a4a)"></div>
  <h3>Hold The Vision</h3>
  <div class="date"><svg width="8" height="8"><rect x=".5" y="1.5" width="7" height="6" fill="none" stroke="#666"/><rect x=".5" y="1.5" width="7" height="2" fill="#666"/></svg>October 2014</div>
  <p>We are told that our thoughts have power and that what we think about we bring aboutrun with stress</p>
  <a class="more" href="#">READ MORE</a><span class="bar"></span>
</article>
<article class="abs card violet" style="left:451px;top:642px">
  <div class="card-photo" role="img" aria-label="Straw hat and open book on the beach" style="background:linear-gradient(180deg,#dfe7ec,#e9dcc4 60%,#d6b98c)"></div>
  <h3>Thinking For Ourselves</h3>
  <div class="date"><svg width="8" height="8"><rect x=".5" y="1.5" width="7" height="6" fill="none" stroke="#666"/><rect x=".5" y="1.5" width="7" height="2" fill="#666"/></svg>October 2014</div>
  <p>We are told that our thoughts have power and that what we think about we bring aboutrun with stress</p>
  <a class="more" href="#">READ MORE</a><span class="bar"></span>
</article>

<aside>
  <div class="abs side-head">OUR BOOKS<i>Shop Online</i></div>
  <div class="abs book-box">
    <div class="book-cover" role="img" aria-label="Book cover of A Small Book of Calm"></div>
    <div class="book-title">A Small Book<br>of Calm</div>
    <div class="book-price">$ 15.00</div>
    <div class="dots"><span></span><span class="on"></span><span></span><span></span></div>
    <a class="book-btn" href="#">SHOP NOW</a>
  </div>

  <div class="abs news">
    <div class="news-title"><svg width="10" height="8"><rect width="10" height="8" fill="#fff"/><path d="M0 0l5 4 5-4" fill="none" stroke="#6c5aa8"/></svg><span>SUBSCRIBE TO <i>NEWSLETTER</i></span></div>
    <div class="news-rule"></div>
    <div class="news-field">Email Address...</div>
    <div class="news-btn">SUBSCRIBE</div>
  </div>

  <div class="abs tabs"><div class="tab-on">UP COMING EVENTS</div><div class="tab-off">WORK SHOPS</div></div>

  <div class="abs event" style="top:688px"><div class="event-date"><div class="m">DEC</div><div class="d">03-2014</div></div><div class="event-text">Lorem ipsum dolor sitamet, consectetuer</div><div class="event-place">Melbourne , Australia</div></div>
  <div class="abs event" style="top:768px"><div class="event-date"><div class="m">DEC</div><div class="d">03-2014</div></div><div class="event-text">Lorem ipsum dolor sitamet, consectetuer</div><div class="event-place">Melbourne , Australia</div></div>
  <div class="abs event" style="top:848px"><div class="event-date"><div class="m">DEC</div><div class="d">03-2014</div></div><div class="event-text">Lorem ipsum dolor sitamet, consectetuer</div><div class="event-place">Melbourne , Australia</div></div>
</aside>

<footer class="abs footer">
  <div class="abs foot-brand"><span class="brand-dot"></span><span class="brand-name">Bright Path Studio</span></div>
  <ul class="abs foot-nav"><li>HOME</li><li>ABOUT US</li><li>BOOKS</li><li>ONLINE STORE</li><li>CONTACT US</li></ul>
  <div class="abs follow">Follow us <span></span></div>
  <div class="abs copyright">Copyright © 2014 brightpathstudio.org</div>
  <div class="abs widget">
    <div class="widget-head">Find us on Chatterly</div>
    <div class="widget-page"><span class="pic"></span><div><div class="name">Bright Path Studio</div><span class="like">Like</span><span class="count">60</span></div></div>
    <div class="post">
      <div class="row"><span class="pic"></span><div><div class="name">Bright Path Studio</div><div class="time">October 4 at 4:24am</div></div></div>
      <p>First world problems #1 I have two hands but I can't hug my kids because I want to put down my smartphone! X</p>
    </div>
    <span class="scroll"></span>
  </div>
</footer>

</body>
</html>
```